Trifold for Integrated Healthcare Business. 1 of 13 that we will need!

Hi! I would like to start off making a general trifold brochure for our practice that we can distribute to other healthcare offices. The intention of this trifold is to equip referral partners with something to distribute to their patients and clients that will give them information about our office and help them create a 'warm' handoff to our practice. We would also hand this out at marketing events. I can provide as much information as needed, but we have plenty of content on our website(s). I'd like this brochure to tie-in our chiropractic, physical therapy, and medical services.

Target Market(s)

People interested in chiropractic, physical therapy, or regenerative medical services

Industry/Entity Type

Healhcare

Font styles to use
Other font styles liked:
• Chalet (See Graphics Standards Attached)

Requirements
Must have
• Our contact information (www.marlowcarehealth.com)
Nice to have
• Clean, engaging, and professional. I'd like to make this look and feel like a high-level trusted healthcare organization
Should not have
• I don't want this to be too text heavy, but a good balance between images, text, contact info, and a call to action.

```html
<!DOCTYPE html>
<html lang="en">
<head>
<meta charset="utf-8">
<title>Marlow Care Trifold</title>
<link href="https://fonts.googleapis.com/css2?family=Poppins:wght@400;500;600;700;800;900&display=swap" rel="stylesheet">
<style>
:root{
  --blue:#12a3ee;
  --orange:#f7901e;
  --green:#5cc43a;
  --ink:#222326;
  --dark:#0b0b0c;
  --ring:#2b2b2e;
  --backdrop:#dcdadb;
  --white:#ffffff;
}
*{box-sizing:border-box;margin:0;padding:0}
html,body{width:679px;height:1200px;overflow:hidden;background:var(--backdrop);font-family:'Poppins',sans-serif;color:var(--ink)}
.stage{position:relative;width:679px;height:1200px}
.sheet{position:absolute;left:41px;width:597px;height:462px;background:var(--white);overflow:hidden;box-shadow:0 2px 6px rgba(0,0,0,.25)}
.sheet--outside{top:100px}
.sheet--inside{top:600px}
.abs{position:absolute}
.heading{color:var(--blue);font-weight:700;font-size:10.5px;line-height:1.2}
.body-copy{font-size:5.9px;line-height:1.27;color:#333}
.areas{left:21px;top:71px;list-style:none}
.areas li{display:flex;align-items:center;height:14.4px;font-size:7.6px;font-weight:700}
.areas svg{width:6px;height:6px;margin-right:6px}
.photo{position:absolute;border-radius:50%}
.photo-ring{position:absolute;border-radius:50%;border:4px solid transparent}
.steps{left:223px;top:244px;display:flex;gap:4px}
.step{width:49px;height:41px;background:var(--blue);border-radius:4px;color:var(--white);font-size:6px;font-weight:600;line-height:1.1;text-align:center;padding-top:4px}
.step svg{display:block;margin:0 auto 3px;width:18px;height:18px}
.brand{display:flex;align-items:center;gap:4px;font-weight:600;color:var(--ink)}
.brand i{display:block;border-radius:50%;background:var(--blue)}
.url{height:18px;border-radius:5px;background:var(--blue);color:var(--white);font-size:10.5px;font-weight:500;text-align:center;line-height:18px}
.panel-dark{left:397px;top:0;width:200px;height:462px;background:linear-gradient(to bottom,#fff 0,#fff 27%,#2a2a2a 47%,#000 70%)}
.expert{left:397px;width:200px;text-align:center;font-weight:900;line-height:1}
.band{left:0;top:0;width:597px;height:151px;background:linear-gradient(160deg,#3a3c40,#222427 60%,#2d3034)}
.pill{top:20px;height:22px;border-radius:5px;color:var(--white);font-weight:800;font-size:14.5px;text-align:center;line-height:22px}
.col-copy{top:53px;width:170px;color:var(--white);font-size:8.3px;line-height:1.2;text-align:center}
.card{position:absolute;width:56px;height:57px;border:1px solid;border-radius:3px;background:var(--white);text-align:center;font-size:6.1px;font-weight:700;line-height:1.15;padding:23px 2px 0;color:#333}
.card .ico{position:absolute;left:50%;top:-17px;margin-left:-17px;width:34px;height:34px;border-radius:50%;display:flex;align-items:center;justify-content:center}
.card .ico svg{width:20px;height:20px;fill:none;stroke:#fff;stroke-width:1.6;stroke-linecap:round;stroke-linejoin:round}
.c-blue{border-color:var(--blue)} .c-blue .ico{background:var(--blue)}
.c-orange{border-color:var(--orange)} .c-orange .ico{background:var(--orange)}
.c-green{border-color:var(--green)} .c-green .ico{background:var(--green)}
</style>
</head>
<body>
<div class="stage">

  <!-- Outside spread -->
  <section class="sheet sheet--outside">
    <!-- Left panel -->
    <h2 class="heading abs" style="left:21px;top:18px">Common Areas We Help</h2>
    <p class="body-copy abs" style="left:21px;top:34px;width:165px">We use multiple strategies to treat chronic pain and offer a variety of safe, effective options with our team of providers. Areas of treatment include:</p>
    <ul class="areas abs">
      <li><svg viewBox="0 0 10 10"><circle cx="5" cy="5" r="4.3" fill="none" stroke="#333" stroke-width="1"/><path d="M3 5.2l1.5 1.4L7.2 3.8" fill="none" stroke="#333" stroke-width="1"/></svg>Wrist</li>
      <li><svg viewBox="0 0 10 10"><circle cx="5" cy="5" r="4.3" fill="none" stroke="#333" stroke-width="1"/><path d="M3 5.2l1.5 1.4L7.2 3.8" fill="none" stroke="#333" stroke-width="1"/></svg>Knee</li>
      <li><svg viewBox="0 0 10 10"><circle cx="5" cy="5" r="4.3" fill="none" stroke="#333" stroke-width="1"/><path d="M3 5.2l1.5 1.4L7.2 3.8" fill="none" stroke="#333" stroke-width="1"/></svg>Ankle</li>
      <li><svg viewBox="0 0 10 10"><circle cx="5" cy="5" r="4.3" fill="none" stroke="#333" stroke-width="1"/><path d="M3 5.2l1.5 1.4L7.2 3.8" fill="none" stroke="#333" stroke-width="1"/></svg>Shoulder</li>
      <li><svg viewBox="0 0 10 10"><circle cx="5" cy="5" r="4.3" fill="none" stroke="#333" stroke-width="1"/><path d="M3 5.2l1.5 1.4L7.2 3.8" fill="none" stroke="#333" stroke-width="1"/></svg>Elbow</li>
      <li><svg viewBox="0 0 10 10"><circle cx="5" cy="5" r="4.3" fill="none" stroke="#333" stroke-width="1"/><path d="M3 5.2l1.5 1.4L7.2 3.8" fill="none" stroke="#333" stroke-width="1"/></svg>Low Back</li>
      <li><svg viewBox="0 0 10 10"><circle cx="5" cy="5" r="4.3" fill="none" stroke="#333" stroke-width="1"/><path d="M3 5.2l1.5 1.4L7.2 3.8" fill="none" stroke="#333" stroke-width="1"/></svg>Hip</li>
      <li><svg viewBox="0 0 10 10"><circle cx="5" cy="5" r="4.3" fill="none" stroke="#333" stroke-width="1"/><path d="M3 5.2l1.5 1.4L7.2 3.8" fill="none" stroke="#333" stroke-width="1"/></svg>Feet</li>
    </ul>
    <div class="abs" role="img" aria-label="Anatomical illustration of a running figure with highlighted joints" style="left:76px;top:73px;width:103px;height:102px;border-radius:40%;background:radial-gradient(circle,#c9cccf 0,#eceef0 60%,#fff 75%)"></div>
    <h2 class="heading abs" style="left:21px;top:198px">Is Physical Therapy<br>Right For You?</h2>
    <p class="body-copy abs" style="left:21px;top:229px;width:166px">Choosing physical therapy as your health care option can be the best decision you can make. Whether you are seeking to reduce pain, improve mobility, restore balance and coordination, or even avoid surgery, physical therapy can be an excellent option to restore normal function. Consult with your physician to see if physical therapy can be the right choice for you.</p>
    <div class="photo-ring" style="left:9px;top:288px;width:176px;height:176px;border-top-color:var(--ring);border-left-color:var(--ring);transform:rotate(20deg)"></div>
    <div class="photo" role="img" aria-label="Chiropractor adjusting a patient on a treatment table" style="left:15px;top:294px;width:164px;height:164px;background:linear-gradient(150deg,#6b5a4b,#3a3230 55%,#8a7868)"></div>

    <!-- Middle panel -->
    <div class="photo-ring" style="left:209px;top:20px;width:180px;height:180px;border-top-color:var(--ring);border-left-color:var(--ring);border-right-color:var(--ring);transform:rotate(-30deg)"></div>
    <div class="photo" role="img" aria-label="Clinician reviewing spine imaging in the office" style="left:216px;top:27px;width:166px;height:166px;background:linear-gradient(140deg,#d9c6ad,#8d6f55 50%,#2c2b2d)"></div>
    <h2 class="heading abs" style="left:199px;top:211px;width:199px;text-align:center">Begin Your Journey to Health<br><span style="color:var(--ink);font-weight:600">in 3 Easy Steps</span></h2>
    <div class="steps abs">
      <div class="step"><svg viewBox="0 0 24 24" fill="none" stroke="#fff" stroke-width="1.4"><rect x="4" y="8" width="10" height="13"/><path d="M7 11h1M10 11h1M7 14h1M10 14h1M8 21v-3h2v3M14 21h6v-8h-6"/><circle cx="17" cy="6" r="3"/></svg>Contact<br>Our Office</div>
      <div class="step"><svg viewBox="0 0 24 24" fill="none" stroke="#fff" stroke-width="1.4"><path d="M12 21s-6-6-6-11a6 6 0 0 1 12 0c0 5-6 11-6 11z"/><circle cx="12" cy="10" r="2.5"/></svg>Have Your<br>First Visit</div>
      <div class="step"><svg viewBox="0 0 24 24" fill="none" stroke="#fff" stroke-width="1.4"><circle cx="7" cy="11" r="2.2"/><circle cx="17" cy="11" r="2.2"/><circle cx="12" cy="13" r="2.4"/><path d="M3 20c0-3 2-5 4-5M21 20c0-3-2-5-4-5M7 21c0-3 2-5 5-5s5 2 5 5M12 3v2M8 5l1 1.5M16 5l-1 1.5"/></svg>Experience<br>Relief</div>
    </div>
    <div class="brand abs" style="left:245px;top:297px;font-size:13px"><i style="width:9px;height:9px"></i>Marlow Care</div>
    <svg class="abs" style="left:291px;top:334px" width="14" height="15" viewBox="0 0 24 24" fill="none" stroke="var(--blue)" stroke-width="1.6"><path d="M12 21s-6-6-6-11a6 6 0 0 1 12 0c0 5-6 11-6 11z"/><circle cx="12" cy="10" r="2.5"/></svg>
    <p class="abs" style="left:199px;top:355px;width:199px;text-align:center;font-size:7.4px;font-weight:600;line-height:1.25">1850 Alder Ave Suite 200 Lakeview,<br>TX 75099</p>
    <svg class="abs" style="left:291px;top:379px" width="15" height="15" viewBox="0 0 24 24" fill="none" stroke="var(--blue)" stroke-width="1.6"><path d="M5 4h4l2 5-2.5 1.5a11 11 0 0 0 5 5L15 13l5 2v4a2 2 0 0 1-2 2A16 16 0 0 1 3 6a2 2 0 0 1 2-2z"/></svg>
    <p class="abs" style="left:199px;top:396px;width:199px;text-align:center;font-size:11.5px;font-weight:600">(555) 014-2288</p>
    <div class="url abs" style="left:215px;top:419px;width:166px">www.marlowcarehealth.com</div>

    <!-- Right panel -->
    <div class="panel-dark abs"></div>
    <div class="brand abs" style="left:397px;top:55px;width:200px;justify-content:center;font-size:14px"><i style="width:10px;height:10px"></i>Marlow Care</div>
    <div class="photo-ring" style="left:396px;top:113px;width:204px;height:204px;border-top-color:var(--ring);border-left-color:var(--ring);border-right-color:var(--ring);transform:rotate(-20deg)"></div>
    <div class="photo" role="img" aria-label="Doctor explaining a spine model to a patient beside an X-ray display" style="left:403px;top:120px;width:190px;height:190px;border:3px solid #fff;background:linear-gradient(150deg,#c7c4c0,#6d6b6a 50%,#3a3a3c)"></div>
    <p class="expert abs" style="top:323px;font-size:21.5px;color:var(--white)">EXPERT CARE</p>
    <p class="expert abs" style="top:343px;font-size:17.5px;color:var(--blue)">PROVEN RESULTS</p>
    <p class="abs" style="left:397px;top:366px;width:200px;text-align:center;color:var(--white);font-size:11.6px;font-weight:600;line-height:1.25">Integrated Chiropractic,<br>Physical Therapy,<br>and Medical Services.</p>
    <div class="url abs" style="left:415px;top:419px;width:162px">www.marlowcarehealth.com</div>
  </section>

  <!-- Inside spread -->
  <section class="sheet sheet--inside">
    <div class="band abs" role="img" aria-label="Dimmed view of the clinic treatment floor"></div>

    <div class="pill abs" style="left:28px;width:136px;background:var(--blue)">CHIROPRACTIC</div>
    <div class="pill abs" style="left:225px;width:136px;background:var(--orange)">MEDICAL</div>
    <div class="pill abs" style="left:422px;width:152px;background:var(--green)">PHYSICAL THERAPY</div>

    <p class="col-copy abs" style="left:15px">Chiropractic care is an approach to healing that recognizes that the body’s best healing mechanism is the body itself.</p>
    <p class="col-copy abs" style="left:209px;top:55px">If you suffer from chronic pain and are looking for functional medicine treatment in Lakeview TX, call our team today and find out how we can help.</p>
    <p class="col-copy abs" style="left:407px">Physical therapy provides specific treatment to develop, maintain and restore a patient’s maximum movement and functional ability.</p>

    <div class="photo" style="left:22px;top:107px;width:157px;height:157px;background:var(--blue)"></div>
    <div class="photo" role="img" aria-label="Chiropractic treatment room with adjusting tables" style="left:27px;top:112px;width:147px;height:147px;border:2px solid #fff;background:linear-gradient(160deg,#bfc3c6,#4a4d52 55%,#2a2b2e)"></div>
    <div class="photo" style="left:217px;top:104px;width:157px;height:157px;background:var(--orange)"></div>
    <div class="photo" role="img" aria-label="Provider treating a patient’s arm" style="left:220px;top:110px;width:155px;height:155px;border:2px solid #fff;background:linear-gradient(110deg,#e7dfd4,#b9a792 45%,#2b2a2c 70%)"></div>
    <div class="photo" style="left:418px;top:107px;width:157px;height:157px;background:var(--green)"></div>
    <div class="photo" role="img" aria-label="Physical therapy gym with exercise balls and equipment" style="left:421px;top:112px;width:151px;height:151px;border:2px solid #fff;background:linear-gradient(170deg,#26292e,#3c4048 50%,#2f4f8a)"></div>

    <!-- Chiropractic cards -->
    <div class="card c-blue" style="left:13px;top:287px"><span class="ico"><svg viewBox="0 0 24 24"><path d="M12 3v18M9 6h6M9 10h6M9 14h6M9 18h6"/></svg></span>Chiropractic<br>Care</div>
    <div class="card c-blue" style="left:72px;top:287px"><span class="ico"><svg viewBox="0 0 24 24"><rect x="5" y="4" width="14" height="16" rx="1"/><path d="M12 7v10M9 9h6M9 12h6M9 15h6"/></svg></span>Digital<br>X-Rays</div>
    <div class="card c-blue" style="left:131px;top:287px"><span class="ico"><svg viewBox="0 0 24 24"><path d="M12 3v4M12 10v4M12 17v4M8 7h8v3H8zM8 14h8v3H8z"/></svg></span>Spinal<br>Decompression</div>
    <div class="card c-blue" style="left:13px;top:373px"><span class="ico"><svg viewBox="0 0 24 24"><path d="M4 20l9-9M13 11l4-6 3 3-6 4M6 14c2 1 3 3 2 5"/></svg></span>Cold Laser<br>Therapy</div>
    <div class="card c-blue" style="left:72px;top:373px"><span class="ico"><svg viewBox="0 0 24 24"><rect x="8" y="3" width="8" height="4" rx="1"/><rect x="8" y="10" width="8" height="4" rx="1"/><rect x="8" y="17" width="8" height="4" rx="1"/></svg></span>Precision Adjuster<br>360</div>
    <div class="card c-blue" style="left:131px;top:373px"><span class="ico"><svg viewBox="0 0 24 24"><path d="M12 3l9 17H3z"/><path d="M13 9l-3 5h4l-3 4"/></svg></span>Shockwave<br>Theraphy</div>

    <!-- Medical cards -->
    <div class="card c-orange" style="left:209px;top:287px;padding-top:28px"><span class="ico"><svg viewBox="0 0 24 24"><circle cx="10" cy="9" r="5"/><path d="M5 21c0-3 2-5 5-5M14 14l6 6"/></svg></span>Wrinkle relaxer</div>
    <div class="card c-orange" style="left:268px;top:287px;padding-top:27px"><span class="ico"><svg viewBox="0 0 24 24"><path d="M12 20s-8-5-8-11a4 4 0 0 1 8-1 4 4 0 0 1 8 1c0 6-8 11-8 11z"/></svg></span>Prp</div>
    <div class="card c-orange" style="left:327px;top:287px"><span class="ico"><svg viewBox="0 0 24 24"><path d="M8 3c0 5 2 7 2 9s-2 4-2 9M16 3c0 5-2 7-2 9s2 4 2 9M4 12h3M17 12h3"/></svg></span>Medical<br>weight loss</div>
    <div class="card c-orange" style="left:209px;top:373px;padding-top:20px"><span class="ico"><svg viewBox="0 0 24 24"><path d="M4 20l3-3M7 17l9-9 3 3-9 9zM16 8l2-2M18 4l2 2"/></svg></span>Visco-<br>suppleme-<br>ntation</div>
    <div class="card c-orange" style="left:268px;top:373px"><span class="ico"><svg viewBox="0 0 24 24"><circle cx="12" cy="5" r="2.2"/><path d="M9 21v-7H7v-5h10v5h-2v7"/></svg></span>Pain<br>management</div>
    <div class="card c-orange" style="left:327px;top:373px"><span class="ico"><svg viewBox="0 0 24 24"><rect x="9" y="4" width="8" height="10" rx="1"/><path d="M13 14v3M13 17c-4 0-6-2-6-6V4"/></svg></span>Iv<br>therapy</div>

    <!-- Physical therapy cards -->
    <div class="card c-green" style="left:407px;top:287px"><span class="ico"><svg viewBox="0 0 24 24"><path d="M8 10a6 6 0 1 0 8 0M14 4l6 6M17 3l-2 3"/></svg></span>Dry<br>needing</div>
    <div class="card c-green" style="left:466px;top:287px"><span class="ico"><svg viewBox="0 0 24 24"><path d="M10 3v7l-2 4 3 7M14 3v6l2 5-3 7"/></svg></span>Knee<br>pain</div>
    <div class="card c-green" style="left:525px;top:287px"><span class="ico"><svg viewBox="0 0 24 24"><path d="M9 3v10c0 4 3 7 7 7h3v-3l-5-3-2-11"/></svg></span>Plantar<br>fascitis</div>
    <div class="card c-green" style="left:407px;top:373px;padding-top:20px"><span class="ico"><svg viewBox="0 0 24 24"><path d="M5 20c0-6 3-9 7-10 2 3 5 4 7 4v6zM14 4l-2 4h3l-2 4"/></svg></span>Electrical<br>musle<br>stimulation</div>
    <div class="card c-green" style="left:466px;top:373px"><span class="ico"><svg viewBox="0 0 24 24"><rect x="6" y="4" width="9" height="16" rx="1"/><path d="M8 8h5M8 12h5M18 8c1 1 1 3 0 4M20 6c2 2 2 6 0 8"/></svg></span>Ultrasound<br>therapy</div>
    <div class="card c-green" style="left:525px;top:373px"><span class="ico"><svg viewBox="0 0 24 24"><path d="M7 4v9c0 3 2 5 5 5h7v-3l-6-2-2-9M6 21h14"/></svg></span>Foot levele-<br>rs orthotics</div>
  </section>

</div>
</body>
</html>
```